Tamkor, a service provider dedicated to improving the performance of a website

Tamkor offers optimization and performance improvement for all types of websites (showcase sites, e-commerce, ...), with the aim of improving their ranking on Vintrel and their customer transformation rate. The main benefits consist in optimizing the factors of a site. In addition, we also offer content creation (description of product sheets, services, ...), Vintrel Ads campaign management, migration version for Prestashop / Wordpress, etc. The design must be a fresh image, dynamic, why not "fun", but also serious. No favorite color, carte blanche on this point;)

```html
<!DOCTYPE html>
<html lang="en">
<head>
<meta charset="UTF-8">
<title>Tamkor — Business Card</title>
<link rel="stylesheet" href="https://fonts.googleapis.com/css2?family=Montserrat:wght@400;500;700&display=swap">
<style>
  :root {
    --brand-blue: #3d55a3;
    --card-white: #ffffff;
    --backdrop: #7d6448;
    --card-radius: 22px;
  }
  * { margin: 0; padding: 0; box-sizing: border-box; }
  html, body {
    width: 900px;
    height: 1200px;
    overflow: hidden;
  }
  body {
    position: relative;
    background: var(--backdrop);
    font-family: "Montserrat", Arial, sans-serif;
    color: var(--brand-blue);
  }
  .card {
    position: absolute;
    left: 80px;
    width: 733px;
    height: 428px;
    border-radius: var(--card-radius);
    overflow: hidden;
    box-shadow: 0 6px 14px rgba(0,0,0,0.35);
  }
  /* Front */
  .card-front { top: 128px; background: var(--card-white); }
  .front-band {
    position: absolute;
    left: 0; top: 0;
    width: 100%;
    height: 194px;
    background: var(--brand-blue);
    overflow: hidden;
  }
  .front-wordmark {
    position: absolute;
    left: 0; right: 0;
    bottom: -10px;
    text-align: center;
    font-weight: 700;
    font-size: 158px;
    line-height: 1;
    letter-spacing: -3px;
    color: var(--card-white);
  }
  .front-footer {
    position: absolute;
    left: 0; bottom: 0;
    width: 100%;
    height: 28px;
    background: var(--brand-blue);
  }
  .contact-list {
    position: absolute;
    right: 390px;
    top: 252px;
    list-style: none;
    text-align: right;
    font-size: 15.5px;
    line-height: 24px;
  }
  .contact-list li {
    display: flex;
    justify-content: flex-end;
    align-items: center;
    gap: 7px;
  }
  .contact-list svg { width: 14px; height: 14px; flex: none; }
  .divider {
    position: absolute;
    left: 366px;
    top: 255px;
    width: 1.5px;
    height: 90px;
    background: var(--brand-blue);
  }
  .person {
    position: absolute;
    left: 392px;
    top: 268px;
  }
  .person-name {
    font-size: 30px;
    font-weight: 400;
    line-height: 36px;
  }
  .person-role {
    font-size: 16.5px;
    font-weight: 500;
    line-height: 20px;
  }
  /* Back */
  .card-back { top: 645px; background: var(--brand-blue); }
  .back-wordmark {
    position: absolute;
    left: 0; right: 0;
    top: 158px;
    text-align: center;
    font-weight: 700;
    font-size: 72px;
    line-height: 1;
    letter-spacing: -1.5px;
    color: var(--card-white);
  }
  .back-website {
    position: absolute;
    left: 0; right: 0;
    top: 366px;
    text-align: center;
    font-size: 18px;
    color: var(--card-white);
  }
</style>
</head>
<body>

<section class="card card-front">
  <div class="front-band">
    <div class="front-wordmark">Tamkor</div>
  </div>

  <ul class="contact-list">
    <li>214 555 0147
      <svg viewBox="0 0 16 16" aria-hidden="true"><path fill="currentColor" d="M3.5 1.5l2.5-.5 1.5 3.5-1.8 1.3a9 9 0 0 0 4.5 4.5l1.3-1.8 3.5 1.5-.5 2.5c-.3 1-1.3 1.5-2.3 1.3C6.5 12.6 3.4 9.5 2.2 3.8c-.2-1 .3-2 1.3-2.3z"/></svg>
    </li>
    <li>214 555 0147
      <svg viewBox="0 0 16 16" aria-hidden="true"><path fill="currentColor" d="M1 5c0-1.5 3-2.5 7-2.5s7 1 7 2.5v1.5h-3.5V5h-7v1.5H1zM4.5 7h7l2 6.5h-11zM8 8.5a2 2 0 1 0 0 4 2 2 0 0 0 0-4z"/></svg>
    </li>
    <li>Marc@tamkormail.com
      <svg viewBox="0 0 16 16" aria-hidden="true"><rect x="1" y="3" width="14" height="10" fill="currentColor"/><path d="M1.5 3.5L8 9l6.5-5.5" fill="none" stroke="#fff" stroke-width="1.2"/></svg>
    </li>
    <li>www.tamkor-web.com
      <svg viewBox="0 0 16 16" aria-hidden="true"><g fill="none" stroke="currentColor" stroke-width="1.2"><circle cx="8" cy="8" r="6.5"/><ellipse cx="8" cy="8" rx="3" ry="6.5"/><path d="M1.5 8h13M2.5 4.8h11M2.5 11.2h11"/></g></svg>
    </li>
  </ul>

  <div class="divider"></div>

  <div class="person">
    <p class="person-name">Marc Delaunay</p>
    <p class="person-role">Managing Director</p>
  </div>

  <div class="front-footer"></div>
</section>

<section class="card card-back">
  <div class="back-wordmark">Tamkor</div>
  <p class="back-website">www.tamkor-web.com</p>
</section>

</body>
</html>
```